Introducing a Personal Care Product called" VELO"

We are a nutra-pharmaceutical company launching a new personal care product called VELO. Some of the products include massage and aroma therapy, as well as personal lubricants. The products will be produced and put into, two bottles that are interlocking so two combinations of products can be purchased at once (i.e. massage and aroma therapy). The poster will be used for promotional advertising, trade shows and for in-store promotions.
Updates

We would like to see a design without the product.

Target Market(s)

Products will be aimed at adults primarily women 18-65 in the USA. We want to appeal to the everyday woman who is interested in their sexual well being.

Industry/Entity Type

Massage

Requirements
Must have
• Clean Presentation. Not many colors. Text should be as follows: VELO for Her....VELO for Him...VELO for You...Let's VELO see attached..Also VELO with Her...Velo with Him..Let's VELO..Open to other copy versions.
Nice to have
• Product image not necessary but can be used. image attached
Should not have
• Too many colors...

```html
<!DOCTYPE html>
<html lang="en">
<head>
<meta charset="utf-8">
<title>velo — poster</title>
<link rel="stylesheet" href="https://fonts.googleapis.com/css2?family=Questrial&display=swap">
<style>
  :root {
    --paper: #ffffff;
    --blush: #f7bfd0;
    --sky: #8cc6f7;
    --ink: #5f5f5f;
    --bottle-rose: #e9a9bb;
    --bottle-azure: #8fc3ee;
    --swirl-rose: #ecc2cd;
    --swirl-silver: #d6e0ea;
  }
  * { margin: 0; padding: 0; box-sizing: border-box; }
  html, body { width: 900px; height: 1200px; overflow: hidden; background: var(--paper); }
  .poster {
    position: relative;
    width: 900px;
    height: 1200px;
    overflow: hidden;
    background: var(--paper);
    font-family: "Questrial", "Century Gothic", sans-serif;
    color: var(--ink);
  }
  .glow {
    position: absolute;
    top: 0;
    width: 450px;
    height: 1200px;
  }
  .glow--her {
    left: 0;
    background: radial-gradient(ellipse 520px 620px at 100% 600px, var(--blush) 0%, rgba(247,191,208,0.55) 45%, rgba(255,255,255,0) 100%);
  }
  .glow--him {
    right: 0;
    background: radial-gradient(ellipse 520px 620px at 0% 600px, var(--sky) 0%, rgba(140,198,247,0.55) 45%, rgba(255,255,255,0) 100%);
  }
  .taglines {
    position: absolute;
    top: 68px;
    left: 0;
    width: 900px;
    text-align: center;
    list-style: none;
  }
  .taglines li {
    font-size: 60px;
    line-height: 80px;
    letter-spacing: 5px;
  }
  .swirl {
    position: absolute;
    top: 295px;
    width: 260px;
    height: 205px;
    border-radius: 50%;
    opacity: 0.6;
  }
  .swirl--left {
    left: 45px;
    background: radial-gradient(ellipse at 70% 50%, var(--swirl-rose) 0%, rgba(236,194,205,0) 70%);
  }
  .swirl--right {
    right: 40px;
    background: radial-gradient(ellipse at 30% 50%, var(--swirl-silver) 0%, rgba(214,224,234,0) 70%);
  }
  .product {
    position: absolute;
    top: 350px;
    left: 218px;
    width: 465px;
    height: 575px;
    border-radius: 22px;
    background: linear-gradient(to right, var(--bottle-rose) 0%, #f6e4ea 30%, #eef4fa 70%, var(--bottle-azure) 100%);
    opacity: 0.85;
  }
  .signoff {
    position: absolute;
    left: 0;
    width: 900px;
    top: 925px;
    text-align: center;
    white-space: nowrap;
    line-height: 1;
  }
  .signoff__lead {
    font-size: 108px;
    letter-spacing: 2px;
  }
  .signoff__brand {
    font-size: 180px;
    letter-spacing: 4px;
    margin-left: 22px;
  }
</style>
</head>
<body>
  <main class="poster">
    <div class="glow glow--her"></div>
    <div class="glow glow--him"></div>

    <ul class="taglines">
      <li>velo for her</li>
      <li>velo for him</li>
      <li>velo for you</li>
    </ul>

    <div class="swirl swirl--left" role="img" aria-label="Rose glitter flourish ornament"></div>
    <div class="swirl swirl--right" role="img" aria-label="Silver glitter flourish ornament"></div>

    <div class="product" role="img" aria-label="Two interlocking clear bottles: a red-capped pink-labelled warming lubricant for her and a blue-capped blue-labelled cooling lubricant for him"></div>

    <p class="signoff">
      <span class="signoff__lead">let’s</span><span class="signoff__brand">velo</span>
    </p>
  </main>
</body>
</html>
```